Anzeigengestaltung für Teppichwäscherei
Zielgruppe
Wir sind eine Teppichwäscherei mit sitz in Recklinghausen.
Wir waschen alle arten von Teppichen vorallem hochwertige perser und designer teppiche.
Zu unserem service gehört auch die Teppichreparatur und restauration von alten und antiken stücken.
unsere zielgruppe sind private haushalte ab 40+ die auch ein teppich zuhause haben.
Aufgabenstellung
es soll modern kreative und auffällig sein aber nicht so das ältere kunden abgeschreckt sind.
folgende sachen müssen drin sein - Teppichreinigung & Teppichreparatur - Kostenlose (gratis ) Abholung und lieferung -
Format: 2sp./100mm & 3sp./100mm & 4sp./225mm
-Normalwäsche statt 19€ jetzt 16 €
-Vollwäsche statt 27€ jetzt 24 €
-Seidenwäsche statt 49€ jetzt 40 €
angebot gilt nur 5 Tage
vom xx.xx.xx bis zum xx.xx.xx

```html
<!DOCTYPE html>
<html lang="de">
<head>
<meta charset="utf-8">
<title>Teppichreinigung &amp; Teppichreparatur – Anzeige</title>
<link href="https://fonts.googleapis.com/css2?family=Arimo:wght@400;700&display=swap" rel="stylesheet">
<style>
  :root {
    --ink: #111111;
    --brand-blue: #1f3a84;
    --paper: #ffffff;
    --rule: #9a9a9a;
    --rug-red: #b8282c;
    --rug-deep: #7a1a1e;
    --rug-navy: #2a2f4a;
    --rug-orange: #d8782a;
    --mist: #d9d6d4;
  }
  html, body {
    margin: 0;
    padding: 0;
    width: 1068px;
    height: 1200px;
    overflow: hidden;
    background: var(--paper);
  }
  .ad {
    position: relative;
    width: 1068px;
    height: 1200px;
    font-family: "Arimo", Arial, sans-serif;
    color: var(--ink);
    background: var(--paper);
    overflow: hidden;
  }
  .hero-photo {
    position: absolute;
    left: 0; top: 0;
    width: 458px; height: 1200px;
    background:
      linear-gradient(160deg, var(--mist) 0%, #cfa9a6 18%, transparent 34%),
      linear-gradient(200deg, transparent 55%, var(--rug-navy) 72%, var(--rug-orange) 82%, var(--rug-red) 92%),
      linear-gradient(180deg, var(--rug-red) 0%, var(--rug-deep) 50%, var(--rug-red) 100%);
  }
  .brand-badge {
    position: absolute;
    left: 48px; top: 930px;
    width: 200px; height: 200px;
    border-radius: 50%;
    background: var(--paper);
    border: 4px solid var(--brand-blue);
    box-shadow: 0 0 0 6px var(--paper);
    display: flex;
    align-items: center;
    justify-content: center;
    box-sizing: border-box;
  }
  .brand-name {
    font-weight: 700;
    font-size: 52px;
    color: var(--brand-blue);
    letter-spacing: 1px;
  }
  .content {
    position: absolute;
    left: 478px; top: 0;
    width: 548px;
  }
  .headline {
    position: absolute;
    top: 40px; left: 0;
    margin: 0;
    font-size: 58px;
    font-weight: 700;
    line-height: 62px;
    white-space: nowrap;
  }
  .subline {
    position: absolute;
    top: 185px; left: 0;
    margin: 0;
    font-size: 31px;
    white-space: nowrap;
  }
  .offer {
    position: absolute;
    left: 0;
    width: 548px;
  }
  .offer-title {
    margin: 0;
    font-size: 31px;
    font-weight: 700;
    line-height: 40px;
  }
  .offer-text {
    margin: 0;
    font-size: 31px;
    line-height: 40px;
    white-space: nowrap;
  }
  .price-bar {
    margin-top: 13px;
    height: 56px;
    background: var(--brand-blue);
    color: var(--paper);
    display: flex;
    align-items: center;
    justify-content: space-between;
    padding: 0 16px 0 18px;
    font-size: 31px;
    box-sizing: border-box;
  }
  .price-bar strong { font-weight: 700; }
  .offer--normal { top: 240px; }
  .offer--full { top: 455px; }
  .offer--silk { top: 670px; }
  .contact {
    position: absolute;
    top: 888px; left: 0;
    margin: 0;
    font-style: normal;
    font-size: 31px;
    line-height: 40px;
  }
  .divider {
    position: absolute;
    top: 1061px; left: 0;
    width: 548px;
    height: 0;
    border-top: 2px solid var(--rule);
  }
  .fine-print {
    position: absolute;
    top: 1072px; left: 0;
    margin: 0;
    width: 548px;
    font-size: 21px;
    line-height: 27px;
  }
</style>
</head>
<body>
<main class="ad">
  <div class="hero-photo" role="img" aria-label="Foto: roter Orientteppich wird mit einem Hochdruckstrahl gereinigt, Schaum und Sprühnebel"></div>

  <div class="brand-badge">
    <span class="brand-name">KVR</span>
  </div>

  <section class="content">
    <h1 class="headline">Teppichreinigung &amp;<br>Teppichreparatur</h1>
    <p class="subline">Kostenlose Abholung und Lieferung</p>

    <div class="offer offer--normal">
      <h2 class="offer-title">Normalwäsche</h2>
      <p class="offer-text">zur Auffrischung Ihres Teppichs und<br>zur Befreiung von Staub und Milben</p>
      <div class="price-bar"><span>Unser Angebot:</span><span><strong>16,00€</strong>/qm</span></div>
    </div>

    <div class="offer offer--full">
      <h2 class="offer-title">Vollwäsche</h2>
      <p class="offer-text">Leistungsumfang Normalwäsche<br>inkl. Imprägnierung/Rückfettung</p>
      <div class="price-bar"><span>Unser Angebot:</span><span><strong>24,00€</strong>/qm</span></div>
    </div>

    <div class="offer offer--silk">
      <h2 class="offer-title">Seidenwäsche</h2>
      <p class="offer-text">Leistungsumfang Vollwäsche inkl.<br>spezielle Seidenveredelung</p>
      <div class="price-bar"><span>Unser Angebot:</span><span><strong>40,00€</strong>/qm</span></div>
    </div>

    <address class="contact">
      Lindenhof-Platz 7<br>
      45657 Recklinghausen<br>
      Tel.: 02361 / 55 210 48<br>
      info@kvr-teppichpflege.de
    </address>

    <div class="divider"></div>
    <p class="fine-print">Angebote gültig vom xx.xx.2024 bis xx.xx.2024. Irrtümer, Druckfehler und Änderungen vorbehal-ten. Preise inkl. MwSt.</p>
  </section>
</main>
</body>
</html>
```